Flyer-Design zum Thema Elektrosmog
Zielgruppe
Wir machen Schlafplatzanalysen auf Elektrosmog.
Elektrosmog entsteht zum Beispiel durch die Stromversorgung im Haus oder durch Funkübertragung wie Mobiltelefon, W-LAN, Bluetooth, etc.
Unsere Zielgruppe sind private Kunden. Im Wesentlichen:
- Frauen mittleren Alters,
- junge Mütter,
- Familien.
Aufgabenstellung
Flyer zum Thema Elektrosmog
Der Flyer soll in Praxen von Heilpraktikern ausgelegt werden oder auch als gezielte Wurfsendung für bestimmte Wohngebiete genutzt werden. Im Prinzip eine Visitenkarte mit Infos.
Faltblatt, geschlossenes Endformat DIN A7 (7,4 x 10,5 cm) / 4 Seiten
Hoch oder quer gefaltet möglich
Bitte Vorschläge zu Papier und Druck
Alternativ:
Produktdetails von Druckwerkel
4/4-farbig (beidseitiger Druck)
Material: 400 g Bilderdruck matt
Veredelung beidseitiger Dispersionslack matt
Seite 1:
Logo: Bogen in gold, Rest schwarz
Text: Erholsam schlafen trotz Elektrosmog für Groß und Klein
Seite 2 und 3 (Innen)
Text:
Fühlen Sie oder Ihre Kinder sich am Morgen trotz ausreichender Schlafdauer müde und zerschlagen?
Elektrosmog kann die Ursache sein.
Wir bieten:
• Ermittlung der Belastung an Ihrem Schlafplatz mit professionellen Messgeräten
• Beratung nach dem Prinzip 1. Abschalten, 2. Abstand, 3. Abschirmen
• Strahlungsarmen und damit erholsamen Schlaf

```html
<!DOCTYPE html>
<html lang="de">
<head>
<meta charset="utf-8">
<title>Ruhepunkt Messtechnik – Faltblatt Elektrosmog</title>
<link rel="stylesheet" href="https://fonts.googleapis.com/css2?family=Fira+Sans:wght@400;600&family=Fira+Sans+Condensed:ital,wght@0,600;1,400;1,600&display=swap">
<style>
  :root {
    --navy: #0b1f4a;
    --gold: #d4a04f;
    --gold-text: #c98f2e;
    --white: #ffffff;
    --stage: #c8c8c8;
    --photo-a: #e7dcd4;
    --photo-b: #f3efec;
    --ink: #0b1f4a;
    --rule: #d9d9d9;
  }
  * { box-sizing: border-box; margin: 0; padding: 0; }
  html, body { width: 1200px; height: 2915px; overflow: hidden; }
  body {
    background: var(--stage);
    font-family: "Fira Sans", sans-serif;
    color: var(--ink);
    position: relative;
  }
  .page { position: absolute; background: var(--white); overflow: hidden; }
  .page svg.shape { position: absolute; inset: 0; }

  .brand-name {
    font-family: "Fira Sans", sans-serif;
    font-weight: 600; font-size: 22px; line-height: 1.1; color: var(--navy);
  }

  /* Title page */
  .cover { width: 412px; height: 586px; }
  .cover .photo {
    position: absolute; left: 0; top: 130px; width: 412px; height: 302px;
    background: linear-gradient(135deg, var(--photo-b), var(--photo-a) 60%, #d6c3b6);
  }
  .cover .brand-name { position: absolute; left: 0; top: 104px; width: 100%; text-align: center; }
  .cover .band { position: absolute; left: 0; top: 432px; width: 100%; height: 10px; background: var(--gold); }
  .cover .claim {
    position: absolute; left: 0; top: 442px; width: 100%; height: 144px;
    background: var(--navy); text-align: center; padding-top: 22px;
    font-family: "Fira Sans Condensed", sans-serif; color: var(--gold);
  }
  .claim-line { font-style: italic; font-weight: 400; font-size: 26px; line-height: 1.25; }
  .claim-line strong { font-weight: 600; }
  .claim-rule { width: 168px; height: 1px; background: var(--gold); margin: 6px auto 8px; }
  .claim-tag { font-style: italic; font-weight: 600; font-size: 18px; color: var(--white); }

  /* Back page */
  .back { width: 412px; height: 585px; }
  .contact { position: absolute; left: 90px; top: 292px; font-size: 16px; line-height: 1.35; }
  .contact .brand-name { font-size: 20px; margin-bottom: 14px; }
  .contact .person { font-weight: 600; }
  .contact .title { font-size: 12px; margin-bottom: 10px; }
  .contact .addr { margin-bottom: 6px; }
  .contact .phone { font-weight: 600; margin-bottom: 6px; }
  .contact .mail { font-weight: 600; }
  .back .foot { position: absolute; left: 0; bottom: 0; width: 100%; height: 24px; background: var(--gold); }

  /* Inside spread */
  .inside { left: 177px; top: 795px; width: 825px; height: 585px; }
  .inside .question {
    position: absolute; left: 40px; top: 408px; width: 340px;
    color: var(--gold-text); font-size: 16px; line-height: 1.35;
  }
  .inside .cause { position: absolute; left: 40px; top: 488px; font-size: 16px; }
  .inside .cause strong { font-size: 20px; font-weight: 600; }
  .inside .divider { position: absolute; left: 413px; top: 40px; width: 1px; height: 500px; background: var(--rule); }
  .offer { position: absolute; left: 440px; top: 56px; width: 360px; }
  .offer h2 { color: var(--gold-text); font-weight: 600; font-size: 21px; margin-bottom: 16px; }
  .offer ul { list-style: none; font-size: 15.5px; line-height: 1.4; }
  .offer li { padding-left: 12px; text-indent: -12px; margin-bottom: 6px; }
  .offer li::before { content: "• "; }
  .steps { position: absolute; left: 440px; top: 196px; width: 360px; display: flex; justify-content: space-between; }
  .step { width: 110px; }
  .step-label { font-family: "Fira Sans Condensed", sans-serif; font-weight: 600; font-size: 16px; margin-bottom: 12px; }
  .step-art { width: 96px; height: 150px; background: linear-gradient(180deg, #f4ebdd, #e9eef7); border-radius: 6px; }
  .inside .slogan {
    position: absolute; left: 430px; top: 488px; width: 340px; text-align: center;
    font-family: "Fira Sans Condensed", sans-serif; font-style: italic; font-weight: 600;
    font-size: 21px; line-height: 1.25; color: var(--gold);
  }

  /* Closed outside spread */
  .outside { left: 181px; top: 2145px; width: 824px; height: 586px; background: transparent; }
  .outside .back { left: 0; top: 0; }
  .outside .cover { left: 412px; top: 0; }
</style>
</head>
<body>

  <!-- Title page -->
  <section class="page cover" style="left:394px; top:134px;">
    <div class="photo" role="img" aria-label="Foto: Familie schläft entspannt im Bett"></div>
    <svg class="shape" width="412" height="586" viewBox="0 0 412 586">
      <path d="M0 0 H412 V136 Q206 206 0 136 Z" fill="var(--white)"/>
      <path d="M0 136 Q206 206 412 136" fill="none" stroke="var(--gold)" stroke-width="4"/>
    </svg>
    <div class="brand-name">Ruhepunkt Messtechnik</div>
    <div class="band"></div>
    <div class="claim">
      <div class="claim-line">Erholsam schlafen</div>
      <div class="claim-line">trotz <strong>ELEKTROSMOG</strong></div>
      <div class="claim-rule"></div>
      <div class="claim-tag">für Groß und Klein</div>
    </div>
  </section>

  <!-- Inside spread -->
  <section class="page inside">
    <svg class="shape" width="825" height="585" viewBox="0 0 825 585">
      <circle cx="195" cy="120" r="228" fill="var(--photo-a)" role="img" aria-label="Foto: Familie liegt müde im Bett und hält den Arm über die Augen"/>
      <circle cx="195" cy="120" r="228" fill="none" stroke="var(--gold)" stroke-width="4"/>
      <path d="M340 585 Q480 360 825 400 V585 Z" fill="var(--navy)"/>
      <path d="M330 585 Q470 350 825 390" fill="none" stroke="var(--gold)" stroke-width="4"/>
    </svg>
    <p class="question">Fühlen Sie oder Ihre Kinder sich am Morgen trotz ausreichender Schlafdauer müde und zerschlagen?</p>
    <p class="cause"><strong>ELEKTROSMOG</strong> kann die Ursache sein.</p>
    <div class="divider"></div>
    <div class="offer">
      <h2>WIR BIETEN IHNEN:</h2>
      <ul>
        <li>Die <strong>Ermittlung</strong> der Belastung an Ihrem Schlafplatz mit professionellen Messgeräten.</li>
        <li>Unsere <strong>Beratung</strong> verläuft nach dem Prinzip:</li>
      </ul>
    </div>
    <div class="steps">
      <div class="step"><div class="step-label">1. Abschalten</div><div class="step-art" role="img" aria-label="Illustration: Schalter und Kopfkissen"></div></div>
      <div class="step"><div class="step-label">2. Abstand</div><div class="step-art" role="img" aria-label="Illustration: Handy und Steckdose mit Abstand zum Kissen"></div></div>
      <div class="step"><div class="step-label">3. Abschirmen</div><div class="step-art" role="img" aria-label="Illustration: Schirmbogen über Kissen mit Teddy"></div></div>
    </div>
    <p class="slogan">... für einen strahlungsarmen<br>und damit erholsamen Schlaf</p>
  </section>

  <!-- Back page -->
  <section class="page back" style="left:383px; top:1483px;">
    <svg class="shape" width="412" height="585" viewBox="0 0 412 585">
      <path d="M0 0 H412 V112 Q170 110 0 210 Z" fill="var(--navy)"/>
      <path d="M0 226 Q170 124 412 124" fill="none" stroke="var(--gold)" stroke-width="6"/>
    </svg>
    <div class="contact">
      <div class="brand-name">Ruhepunkt Messtechnik</div>
      <div class="person">Sabine Lorenzen</div>
      <div class="person">Matthias Lorenzen</div>
      <div class="title">Dipl-Ing. (FH) der Elektrotechnik</div>
      <div class="addr">Lindenweg 17<br>64521 Wiesental</div>
      <div class="phone">06152 481 230</div>
      <div class="mail">wellruhig@postfach.de</div>
    </div>
    <div class="foot"></div>
  </section>

  <!-- Outside spread -->
  <section class="page outside">
    <div class="page back">
      <svg class="shape" width="412" height="585" viewBox="0 0 412 585">
        <path d="M0 0 H412 V112 Q170 110 0 210 Z" fill="var(--navy)"/>
        <path d="M0 226 Q170 124 412 124" fill="none" stroke="var(--gold)" stroke-width="6"/>
      </svg>
      <div class="contact">
        <div class="brand-name">Ruhepunkt Messtechnik</div>
        <div class="person">Sabine Lorenzen</div>
        <div class="person">Matthias Lorenzen</div>
        <div class="title">Dipl-Ing. (FH) der Elektrotechnik</div>
        <div class="addr">Lindenweg 17<br>64521 Wiesental</div>
        <div class="phone">06152 481 230</div>
        <div class="mail">wellruhig@postfach.de</div>
      </div>
      <div class="foot"></div>
    </div>
    <div class="page cover">
      <div class="photo" role="img" aria-label="Foto: Familie schläft entspannt im Bett"></div>
      <svg class="shape" width="412" height="586" viewBox="0 0 412 586">
        <path d="M0 0 H412 V136 Q206 206 0 136 Z" fill="var(--white)"/>
        <path d="M0 136 Q206 206 412 136" fill="none" stroke="var(--gold)" stroke-width="4"/>
      </svg>
      <div class="brand-name">Ruhepunkt Messtechnik</div>
      <div class="band"></div>
      <div class="claim">
        <div class="claim-line">Erholsam schlafen</div>
        <div class="claim-line">trotz <strong>ELEKTROSMOG</strong></div>
        <div class="claim-rule"></div>
        <div class="claim-tag">für Groß und Klein</div>
      </div>
    </div>
  </section>

</body>
</html>
```